Corporate Comedy Poster Brochure

I have designed an 10.75 by 15 flat one-sided poster/flyer to mail out for promoting my corporate comedy services. I don't think I did a bad job, but would love to see if someone can create something else for the same purpose, but with an expert hand and eye, as I am not a designer by trade. You should get a sense of it by the PSD example I provided.

FYI: My websites are:
www.paulvantrimm.com/corporate-comedian
www.gigsforstaffnights.com

Target Market(s)

Event Planners, Chambers of Commerce, Human Resources people who might be in charge of the company party, Golf Courses, Banquet Facilities, etc.

Industry/Entity Type

Entertainment Industry

Font styles to use
Sans Serif

Requirements
Must have
• Must have the textual content, headshot, and all logos that are in the PSD I provided.
• 10.75 inches by 15 inches at 300dpi.
• The PSD is on my Stashbox Cloud at :https://files.stashboxcloud.com/file/d/7Kq41mzvtp3WyhaR8cLn2JsXeQ60/view?usp=sharing
• I promise there is no virus or you know who's website to take down, :-)
Nice to have
• 1) Would be nice to have final in Photoshop, as I could then make adjustments easier. I don't know Illustrator well.
• 2) My motif is a poster for a show that is really a flyer promoting the fact that I perform shows. You can stick with this motif, or if you have a better motif, I am open to that.

```html
<!DOCTYPE html>
<html lang="en">
<head>
<meta charset="utf-8">
<title>Comedy Night with Paul Van Trimm</title>
<link rel="stylesheet" href="https://fonts.googleapis.com/css2?family=Anton&family=Open+Sans:ital,wght@0,400;0,600;0,700;0,800;1,600;1,700&display=swap">
<style>
  :root {
    --navy: #0b2a6b;
    --blue-deep: #0d3e9c;
    --blue-mid: #1b63d1;
    --blue-light: #5fb1f2;
    --yellow: #ffe21a;
    --ink: #111827;
    --white: #ffffff;
  }
  * { box-sizing: border-box; margin: 0; padding: 0; }
  html, body { width: 870px; height: 1200px; overflow: hidden; background: #e9e9e9; }
  .poster {
    position: relative; width: 870px; height: 1200px; overflow: hidden;
    font-family: "Open Sans", Arial, sans-serif;
    background: radial-gradient(ellipse at 55% 38%, var(--blue-light) 0%, var(--blue-mid) 38%, var(--blue-deep) 75%, var(--navy) 100%);
  }
  .title {
    position: absolute; top: 22px; left: 0; width: 100%; text-align: center;
    font-family: "Anton", Impact, sans-serif; font-size: 118px; line-height: 1;
    color: var(--yellow); letter-spacing: 2px;
    -webkit-text-stroke: 4px var(--ink); paint-order: stroke fill;
    text-shadow: 4px 5px 0 var(--ink);
  }
  .venue-tag {
    position: absolute; top: 172px; left: 26px; padding: 10px 20px;
    background: var(--white); border: 4px solid var(--navy); border-radius: 14px;
    font-family: "Anton", Impact, sans-serif; font-size: 50px; line-height: 1; color: var(--blue-deep);
  }
  .headliner {
    position: absolute; top: 182px; left: 336px; color: var(--white); white-space: nowrap;
    font-weight: 800; font-size: 50px; line-height: 1; letter-spacing: -1px;
    text-shadow: 3px 3px 0 var(--navy);
  }
  .headliner .with { font-style: italic; font-weight: 700; font-size: 24px; vertical-align: middle; margin-right: 6px; letter-spacing: 0; }
  .media-row { position: absolute; top: 254px; right: 24px; display: flex; gap: 18px; align-items: center; }
  .media-mark { display: flex; align-items: center; gap: 6px; font-weight: 700; font-size: 17px; color: var(--white); }
  .media-mark .dot { width: 24px; height: 24px; border-radius: 50%; background: var(--white); }
  .headshot {
    position: absolute; left: 40px; top: 280px; width: 290px; height: 740px;
    border-radius: 120px 120px 20px 20px;
    background: linear-gradient(180deg, #2a2a33 0%, #1d1d24 45%, #3e5a86 62%, #2f4770 90%, #5a3a24 100%);
  }
  .pitch {
    position: absolute; top: 310px; left: 340px; width: 516px; padding: 12px 14px;
    background: var(--yellow); border: 3px solid var(--ink);
    font-weight: 800; font-size: 25px; line-height: 1.2; color: var(--navy); text-align: center;
  }
  .quotes { position: absolute; top: 420px; left: 370px; width: 470px; color: var(--yellow); }
  .quote { font-style: italic; font-weight: 600; font-size: 20px; line-height: 1.3; }
  .quote cite { display: block; text-align: right; font-style: italic; margin-top: 4px; }
  .quote + .quote { margin-top: 22px; }
  .occasions {
    position: absolute; top: 690px; left: 350px; width: 500px; padding: 16px 20px;
    background: var(--white); border: 4px solid var(--navy); border-radius: 16px;
    display: grid; grid-template-columns: 1fr 1fr; row-gap: 10px; column-gap: 14px;
    list-style: none; font-weight: 700; font-size: 18px; color: var(--navy);
  }
  .occasions li { display: flex; align-items: center; gap: 10px; white-space: nowrap; }
  .occasions li::before {
    content: ""; width: 18px; height: 18px; border-radius: 50%;
    background: var(--yellow); border: 2px solid var(--navy); flex: none;
  }
  .contact { position: absolute; top: 860px; right: 26px; text-align: right; color: var(--white); }
  .contact h2 { font-weight: 800; font-size: 28px; margin-bottom: 10px; }
  .contact-line { display: flex; justify-content: flex-end; align-items: center; gap: 10px; font-weight: 600; font-size: 19px; margin-top: 6px; }
  .contact-line.split { justify-content: space-between; gap: 40px; }
  .contact-line svg { width: 20px; height: 20px; flex: none; }
  .clients {
    position: absolute; left: 0; bottom: 0; width: 100%; height: 150px;
    background: var(--white); border-top: 5px solid var(--navy);
    display: flex; align-items: center; padding: 0 22px; gap: 18px;
  }
  .clients-label { width: 120px; font-weight: 800; font-size: 19px; line-height: 1.15; color: var(--navy); }
  .client-grid { flex: 1; display: grid; grid-template-columns: repeat(6, 1fr); row-gap: 18px; column-gap: 10px; align-items: center; }
  .client { display: flex; align-items: center; gap: 5px; font-weight: 800; font-size: 16px; color: var(--navy); white-space: nowrap; }
  .client .sq { width: 12px; height: 12px; background: var(--navy); flex: none; }
  .client-note { grid-column: span 2; font-size: 12px; font-weight: 600; line-height: 1.2; color: var(--ink); }
</style>
</head>
<body>
<main class="poster">
  <h1 class="title">COMEDY NIGHT</h1>
  <div class="venue-tag">@Your Event</div>
  <div class="headliner"><span class="with">with</span>Paul Van Trimm</div>

  <div class="media-row">
    <span class="media-mark"><span class="dot"></span>LaughLine TV</span>
    <span class="media-mark"><span class="dot"></span>Orbitwave Radio</span>
  </div>

  <div class="headshot" role="img" aria-label="Full-length photo of the comedian in a dark sweater and jeans"></div>

  <p class="pitch">Hilarious entertainment for any corporate, club or dinner event!</p>

  <div class="quotes">
    <blockquote class="quote">"Your show was AMAZING!!! People were telling me for days how much fun they had and how great they thought you were."<cite>-Keystone Mutual Insurance</cite></blockquote>
    <blockquote class="quote">"Paul, I can not tell you how well the evening went. This was the perfect first time comedy event."<cite>-Maplewood Country Club</cite></blockquote>
  </div>

  <ul class="occasions">
    <li>Holiday Parties</li>
    <li>Country Clubs</li>
    <li>Awards Banquets</li>
    <li>Community Shows</li>
    <li>Dinner Shows</li>
    <li>Fundraisers</li>
  </ul>

  <div class="contact">
    <h2>For More Information:</h2>
    <div class="contact-line split">
      <span>555-014-2286</span>
      <span style="display:flex;align-items:center;gap:10px">
        <svg viewBox="0 0 20 20" aria-hidden="true"><circle cx="10" cy="10" r="8" fill="none" stroke="#fff" stroke-width="2"/><path d="M2 10h16M10 2c3 3 3 13 0 16M10 2c-3 3-3 13 0 16" fill="none" stroke="#fff" stroke-width="1.5"/></svg>
        www.paulvantrimm.com
      </span>
    </div>
    <div class="contact-line">
      <svg viewBox="0 0 20 20" aria-hidden="true"><rect x="2" y="4" width="16" height="12" rx="1" fill="none" stroke="#fff" stroke-width="2"/><path d="M2 5l8 6 8-6" fill="none" stroke="#fff" stroke-width="2"/></svg>
      comedian@paulvantrimm.com
    </div>
  </div>

  <section class="clients">
    <div class="clients-label">Some Previous Satisfied Clients:</div>
    <div class="client-grid">
      <span class="client"><span class="sq"></span>Harvestline</span>
      <span class="client">Grainco</span>
      <span class="client"><span class="sq"></span>Skyvale Air</span>
      <span class="client">Keystone</span>
      <span class="client">Surecove</span>
      <span class="client">Freshmart</span>
      <span class="client">Orchard Grill</span>
      <span class="client"><span class="sq"></span>Buildwell</span>
      <span class="client">Tellaro</span>
      <span class="client">Royal Fern</span>
      <span class="client-note">And many other companies, country clubs and associations both large and small.</span>
    </div>
  </section>
</main>
</body>
</html>
```